Artificial Intelligence based service Veltranoquest.ai

Looking for a website for service designed for driving schools to deliver AI based solutions and features. File are to include various pages from contact to list of services to faqs, demos and more. we are looking for a website for AI based service for driving schools. services will include things like chat bots, voice agent, document processing and ai based marketing.

Target Market(s)

driving school owners and managers.

Industry/Entity Type

software and AI

Number of Pages Required

4 page

Font styles to use
Sans Serif

Requirements
Must have
• clean and easy to navigate pages. responsive. also delivery via FIGMA.

```html
<!DOCTYPE html>
<html lang="en">
<head>
<meta charset="utf-8">
<title>Veltranoquest.ai — AI for Driving Schools</title>
<link href="https://fonts.googleapis.com/css2?family=Nunito+Sans:wght@400;600;700;800&display=swap" rel="stylesheet">
<style>
:root{
  --navy:#0d2147;
  --navy-btn:#0a1f44;
  --demo:#124a72;
  --text:#333;
  --muted:#555;
  --soft:#f8f8f8;
  --white:#fff;
  --green:#7dbd7d;
  --footer:#333;
  --footer-head:#6cbd6c;
  --footer-text:#dcdcdc;
}
*{box-sizing:border-box;margin:0;padding:0}
html,body{width:734px;height:1200px;overflow:hidden}
body{font-family:"Nunito Sans",sans-serif;color:var(--text);background:var(--white);position:relative}
.site-header{position:absolute;top:0;left:0;width:734px;height:46px;background:var(--white)}
.brand{position:absolute;left:52px;top:14px;display:flex;align-items:center;gap:4px;font-size:11px;font-weight:700;color:var(--navy)}
.brand-square{width:9px;height:9px;background:var(--navy)}
.main-nav{position:absolute;top:18px;left:247px}
.main-nav a{position:absolute;font-size:8.5px;color:var(--text);text-decoration:none;white-space:nowrap}
.demo-btn{position:absolute;left:614px;top:11px;width:59px;height:24px;background:var(--demo);color:#fff;border-radius:3px;font-size:8.5px;font-weight:600;display:flex;align-items:center;justify-content:center}
.accent-bar{position:absolute;top:46px;left:0;width:734px;height:7px;background:linear-gradient(90deg,#0b2346 0%,#1d4f86 55%,#4a9ad6 100%)}
.band{position:absolute;left:0;width:734px}
.band.soft{background:var(--soft)}
.section-title{position:absolute;left:0;width:734px;display:flex;justify-content:center;align-items:center;gap:9px;font-size:18.5px;font-weight:800;color:var(--navy);line-height:1}
.section-sub{position:absolute;left:0;width:734px;text-align:center;font-size:8.3px;color:var(--muted)}
.card{position:absolute;width:196px;background:var(--white);border-radius:4px;box-shadow:0 1px 6px rgba(0,0,0,.06);padding:17px 8px 0 16px}
.card h3{font-size:11.7px;font-weight:800;color:#2b2b2b;margin-bottom:9px}
.card p{font-size:8px;line-height:13.6px;color:#333;letter-spacing:-.05px}
.plan{position:absolute;top:774px;width:196px;height:248px;background:var(--white);border-radius:4px;box-shadow:0 1px 6px rgba(0,0,0,.05);text-align:center;padding-top:23px}
.plan.featured{border:1px solid var(--green)}
.badge{position:absolute;top:-8px;left:50%;transform:translateX(-50%);background:var(--green);color:#fff;font-size:7px;font-weight:700;padding:3px 7px;border-radius:9px;white-space:nowrap}
.plan h4{font-size:9.7px;font-weight:700;color:#2b2b2b;line-height:13px}
.plan .tag{font-size:8.3px;color:#333;line-height:14px}
.price{margin-top:14px;height:34px;font-size:25px;font-weight:800;color:var(--navy);line-height:34px}
.price span{font-size:8.3px;font-weight:400;color:#666}
.plan ul{list-style:none;margin-top:5px;font-size:8.3px;line-height:13.6px;color:#333}
.plan-btn{display:inline-block;margin-top:8px;width:64px;height:24px;line-height:24px;background:var(--navy-btn);color:#fff;font-size:8.3px;font-weight:600;border-radius:2px}
.plan-btn.wide{width:73px}
.plan-btn.green{background:var(--green)}
.custom-note{position:absolute;top:1045px;left:0;width:734px;text-align:center;font-size:8.3px;color:#333}
.quote-btn{position:absolute;top:1066px;left:318px;width:109px;height:23px;background:var(--navy-btn);color:#fff;font-size:8.3px;font-weight:600;border-radius:2px;display:flex;align-items:center;justify-content:center}
.site-footer{position:absolute;top:1100px;left:0;width:734px;height:100px;background:var(--footer)}
.foot-col{position:absolute;top:28px;width:120px}
.foot-col h5{font-size:9.7px;font-weight:700;color:var(--footer-head);margin-bottom:10px}
.foot-col li{list-style:none;font-size:8.3px;line-height:19px;color:var(--footer-text)}
.foot-col p{font-size:8.3px;line-height:14.5px;color:#f0f0f0;width:112px}
</style>
</head>
<body>
<header class="site-header">
  <div class="brand"><span class="brand-square"></span>Veltranoquest.ai</div>
  <nav class="main-nav">
    <a style="left:0">Solutions</a>
    <a style="left:50px">Features</a>
    <a style="left:97px">Benefits</a>
    <a style="left:141px">Pricing</a>
    <a style="left:182px">FAQ</a>
    <a style="left:213px">Contact</a>
  </nav>
  <div class="demo-btn">Get Demo</div>
</header>
<div class="accent-bar"></div>

<section class="band" style="top:53px;height:175px">
  <h2 class="section-title" style="top:8px">
    <svg width="18" height="14" viewBox="0 0 18 14"><ellipse cx="10" cy="6" rx="8" ry="5.5" fill="#e6dcf5"/><path d="M3 9 L1 13 L6 10Z" fill="#e6dcf5"/></svg>
    AI Chat Assistant for Driving Schools
  </h2>
  <p class="section-sub" style="top:39px">Handle student inquiries anytime, anywhere with our multilingual chatbot solution.</p>
</section>
<div class="card" style="left:63px;top:129px;height:99px"><h3>Website Chat</h3><p>Engage visitors on your website with instant answers to common questions about your programs, pricing, and requirements.</p></div>
<div class="card" style="left:275px;top:129px;height:99px"><h3>SMS Texting</h3><p>Students can text questions and get instant responses, perfect for quick scheduling questions or reminders.</p></div>
<div class="card" style="left:486px;top:129px;height:99px"><h3>Social Media</h3><p>Integrates with Chatterly Messenger, Snapfolio, and other platforms to handle inquiries from all channels.</p></div>

<section class="band soft" style="top:228px;height:249px">
  <h2 class="section-title" style="top:50px">
    <svg width="16" height="19" viewBox="0 0 16 19"><path d="M1 1h10l4 4v13H1Z" fill="#ece4f6"/><path d="M11 1v4h4" fill="#d8cbe9"/><path d="M4 9h8M4 11.5h8M4 14h6" stroke="#b9abcc" stroke-width=".8"/></svg>
    AI Document Processing
  </h2>
  <p class="section-sub" style="top:83px">Automate your paperwork and reduce administrative headaches.</p>
</section>
<div class="card" style="left:63px;top:349px;height:85px"><h3>License Verification</h3><p>Automatically verify student permits and licenses by scanning documents.</p></div>
<div class="card" style="left:275px;top:349px;height:85px"><h3>Form Processing</h3><p>Extract data from registration forms, waivers, and other paperwork instantly.</p></div>
<div class="card" style="left:486px;top:349px;height:85px"><h3>Payment Processing</h3><p>Securely process payments and payment plans with automated reminders.</p></div>

<section class="band" style="top:477px;height:177px">
  <h2 class="section-title" style="top:7px">
    <svg width="20" height="19" viewBox="0 0 20 19"><rect x="1" y="1" width="18" height="17" rx="2" fill="#ebe5f4"/><path d="M1 6h18M1 11h18M6 1v17M11 1v17" stroke="#d6cbe6" stroke-width=".6"/><path d="M2 15 L7 10 L10 12 L18 4" stroke="#3d7fc9" stroke-width="1.6" fill="none"/></svg>
    AI-Powered Marketing
  </h2>
  <p class="section-sub" style="top:41px">Smart tools to help you attract more students and grow your business.</p>
</section>
<div class="card" style="left:63px;top:555px;height:98px"><h3>Lead Generation</h3><p>AI identifies and targets your ideal students across digital channels.</p></div>
<div class="card" style="left:275px;top:555px;height:98px"><h3>Dynamic Ads</h3><p>Automatically creates and optimizes ads based on what's working best.</p></div>
<div class="card" style="left:486px;top:555px;height:98px"><h3>Review Management</h3><p>Automatically requests reviews from happy students and helps manage your online reputation.</p></div>

<section class="band soft" style="top:654px;height:446px">
  <h2 class="section-title" style="top:49px">Simple, Transparent Pricing</h2>
  <p class="section-sub" style="top:82px">Choose the plan that fits your driving school's needs.</p>
</section>
<div class="plan" style="left:63px">
  <h4>Starter</h4><p class="tag">Perfect for small driving schools</p>
  <div class="price">$99<span>/month</span></div>
  <ul><li>Voice Agent - 500 mins</li><li>Basic Chatbot</li><li>Email Support</li><li>Up to 50 students/mo</li></ul>
  <span class="plan-btn">Get Started</span>
</div>
<div class="plan featured" style="left:275px">
  <span class="badge">Most Popular</span>
  <h4>Professional</h4><p class="tag">Ideal for growing schools</p>
  <div class="price">$249<span>/month</span></div>
  <ul><li>Voice Agent - 1500 mins</li><li>Advanced Chatbot</li><li>Priority Support</li><li>Document Processing</li><li>Up to 200 students/mo</li></ul>
  <span class="plan-btn green">Get Started</span>
</div>
<div class="plan" style="left:486px">
  <h4>Enterprise</h4><p class="tag">For large driving schools</p>
  <div class="price">$499<span>/month</span></div>
  <ul><li>Unlimited Voice Agent</li><li>Premium Chatbot</li><li>24/7 Support</li><li>Full Document System</li><li>AI Marketing Tools</li><li>Unlimited Students</li></ul>
  <span class="plan-btn wide">Contact Sales</span>
</div>
<p class="custom-note">Need custom solutions? We offer tailored packages for multi-location schools.</p>
<div class="quote-btn">Request Custom Quote</div>

<footer class="site-footer">
  <div class="foot-col" style="left:63px"><h5>Veltrano</h5><p>AI-powered solutions designed specifically to help driving schools automate</p></div>
  <div class="foot-col" style="left:190px"><h5>Solutions</h5><ul><li>Voice Agent</li><li>AI Chat Assistant</li><li>Document Processing</li></ul></div>
  <div class="foot-col" style="left:316px"><h5>Company</h5><ul><li>About Us</li><li>Careers</li><li>Blog</li></ul></div>
  <div class="foot-col" style="left:442px"><h5>Resources</h5><ul><li>FAQ</li><li>Support</li><li>Case Studies</li></ul></div>
  <div class="foot-col" style="left:567px;width:160px"><h5>Contact</h5><ul><li>48 Orbit Lane</li><li>Fremont, CA 94538</li><li>hello@veltranoquest.ai</li></ul></div>
</footer>
</body>
</html>
```